The Marlowe Method Diet Business Card

The Marlowe Method is a revolutionary new diet approach. We need a fresh, different business card design for The Marlowe Method. We would like the cards lettering and designed match with the color scheme of the logo(Orange,black,grey) and the website. We would like the front of the business card to be the pic of a scale(that people weigh themselves on).We have attached a pic we would like that kind of old school number scale. With the the words "want to lose weight?Eat what you crave! Change how it's made! Get moving! No gym required. Similar to our shirt design. At the Back of the card we would like our logo. My name Dennis Farrow Jr. My telephone number 504-617-2253 my email dfarrowjr@marlowemethod-example.com

Target Market(s)

Everyone who's looking to get into shape

Industry/Entity Type

Health And Wellness

Contact Information for Business Card

Name , company logo, weight scale. Want to have something people talk about that looks so refreshing

Colors
faa54b
f68d4d
000000
b2b2b2

Requirements
Must have
• Weight scale, logo and futuristic look. Nothing plain get creative baby!
Nice to have
• Something that would stand out in a crowd
Should not have
• Be boring or look like any other card or be anything like Brenner diet cards

```html
<!DOCTYPE html>
<html lang="en">
<head>
<meta charset="utf-8">
<title>The Marlowe Method – Business Card</title>
<link rel="stylesheet" href="https://fonts.googleapis.com/css2?family=Mulish:wght@400;700&display=swap">
<style>
  :root {
    --orange: #f68d2e;
    --orange-light: #faa54b;
    --orange-deep: #f47f1e;
    --ink: #000000;
    --grey: #b2b2b2;
    --grey-dark: #555555;
    --text-grey: #4a4a4a;
    --paper: #ffffff;
    --backdrop: #3a3a3a;
  }
  * { box-sizing: border-box; margin: 0; padding: 0; }
  html, body {
    width: 1105px;
    height: 1200px;
    overflow: hidden;
    background: var(--backdrop);
    font-family: "Mulish", sans-serif;
  }
  .canvas { position: relative; width: 1105px; height: 1200px; }

  .card {
    position: absolute;
    left: 196px;
    width: 720px;
    height: 412px;
    overflow: hidden;
  }

  /* Contact side */
  .card--contact { top: 145px; background: var(--paper); }
  .brand {
    position: absolute;
    left: 70px;
    top: 178px;
    display: flex;
    align-items: center;
    gap: 12px;
  }
  .brand__dot {
    width: 30px; height: 30px;
    border-radius: 50%;
    background: var(--orange);
  }
  .brand__name {
    font-weight: 700;
    font-size: 22px;
    color: var(--text-grey);
    white-space: nowrap;
  }
  .contact {
    position: absolute;
    left: 360px;
    top: 138px;
  }
  .contact__name {
    font-weight: 700;
    font-size: 26px;
    color: var(--orange);
    margin-bottom: 14px;
  }
  .contact__list { list-style: none; }
  .contact__item {
    display: flex;
    align-items: center;
    gap: 12px;
    font-size: 18px;
    color: var(--text-grey);
    height: 31px;
  }
  .contact__icon { width: 18px; height: 18px; flex: none; }
  .card__rule {
    position: absolute;
    left: 0; right: 0;
    top: 376px;
    height: 3px;
    background: var(--grey-dark);
  }
  .card__band {
    position: absolute;
    left: 0; right: 0;
    top: 381px;
    bottom: 0;
    background: linear-gradient(90deg, var(--orange-deep), var(--orange-light) 50%, var(--orange-deep));
  }

  /* Message side */
  .card--message {
    top: 602px;
    background: radial-gradient(ellipse at 55% 50%, #fbb061 0%, var(--orange-light) 35%, var(--orange-deep) 100%);
  }
  .scale-art {
    position: absolute;
    left: 124px;
    top: 109px;
    width: 134px;
    height: 194px;
    border-radius: 26px 26px 20px 20px;
    background: linear-gradient(180deg, #d8d8d8 0%, #8a8a8a 30%, #2a2a2a 60%, #111111 100%);
  }
  .message {
    position: absolute;
    left: 342px;
    top: 118px;
    color: var(--paper);
  }
  .message__title {
    font-weight: 700;
    font-size: 23px;
    letter-spacing: 0.5px;
    margin-bottom: 10px;
  }
  .message__line {
    font-size: 21px;
    line-height: 36px;
  }
</style>
</head>
<body>
<div class="canvas">

  <section class="card card--contact">
    <div class="brand">
      <span class="brand__dot"></span>
      <span class="brand__name">The Marlowe Method</span>
    </div>

    <div class="contact">
      <h1 class="contact__name">Dennis Farrow Jr.</h1>
      <ul class="contact__list">
        <li class="contact__item">
          <svg class="contact__icon" viewBox="0 0 24 24"><path fill="var(--orange)" d="M6.6 10.8a15.1 15.1 0 0 0 6.6 6.6l2.2-2.2a1 1 0 0 1 1-.25 11.4 11.4 0 0 0 3.6.57 1 1 0 0 1 1 1V20a1 1 0 0 1-1 1A17 17 0 0 1 3 4a1 1 0 0 1 1-1h3.5a1 1 0 0 1 1 1c0 1.25.2 2.45.57 3.57a1 1 0 0 1-.25 1z"/></svg>
          504-617-2253
        </li>
        <li class="contact__item">
          <svg class="contact__icon" viewBox="0 0 24 24"><rect x="2" y="5" width="20" height="14" rx="1" fill="var(--orange)"/><path d="M3 6l9 7 9-7" fill="none" stroke="#fff" stroke-width="1.8"/></svg>
          dfarrowjr@marlowemethod-example.com
        </li>
        <li class="contact__item">
          <svg class="contact__icon" viewBox="0 0 24 24"><circle cx="12" cy="12" r="10" fill="var(--orange)"/><path d="M2 12h20M12 2c3 3 3 17 0 20M12 2c-3 3-3 17 0 20" fill="none" stroke="#fff" stroke-width="1.4"/></svg>
          www.marlowemethod-example.com
        </li>
      </ul>
    </div>

    <div class="card__rule"></div>
    <div class="card__band"></div>
  </section>

  <section class="card card--message">
    <div class="scale-art" role="img" aria-label="Illustration of a classic dial bathroom scale with a silver dial and black platform"></div>
    <div class="message">
      <h2 class="message__title">WANT TO LOSE WEIGHT?</h2>
      <p class="message__line">Eat what you crave!</p>
      <p class="message__line">Change how it's made!</p>
      <p class="message__line">Get moving!</p>
      <p class="message__line">No gym required.</p>
    </div>
  </section>

</div>
</body>
</html>
```